Trade show banner and popup for Plexa Works

Use the existing logo and graphic elements and text of sales arguments from our web site www.plexaworks-demo.com to create a backdrop banner and popup banner.

Both banners are trim size 181.7 x 76.2 cm. One is vertical, the other is horizontal. The full bleed size is 767 x 1824 mm 2265 x 5385 pixels.

We have a 2m by 2m corner stand on a tradeshow. The banner will be on one wall, the vertical against the other wall by the aisle.

Target Market(s)

This display is for a manufacturing trade show. The typical visitors are middle age engineers.

Industry/Entity Type

Trade

Requirements
Must have
• Our logo.
Nice to have
• One of the main benefits of our system is that it can be created for no charge with an online signup which is available at the show. We want to tempt people off the aisles to do this. So the vertical banner could have the words "Create your own online ERP system here for no charge"
Should not have
• Small text, these banners should attract attention of passers by in a trade show.

```html
<!DOCTYPE html>
<html lang="en">
<head>
<meta charset="utf-8">
<title>Plexa Works – Trade Show Banner</title>
<link rel="stylesheet" href="https://fonts.googleapis.com/css2?family=Open+Sans:ital,wght@0,400;0,600;0,700;1,400&display=swap">
<style>
  :root {
    --sky-top: #3f9fe2;
    --sky-mid: #5aafe6;
    --sky-low: #9cc8e6;
    --horizon: #c9dbe8;
    --sea: #6f8fa6;
    --sand: #d9c7a8;
    --white: #ffffff;
    --ink: #2b2a27;
    --tagline: #f4e46a;
    --url: #1c2a35;
  }
  html, body {
    margin: 0;
    padding: 0;
    width: 1200px;
    height: 2856px;
    overflow: hidden;
    background: var(--white);
  }
  .banner {
    position: relative;
    width: 1200px;
    height: 2856px;
    overflow: hidden;
    font-family: "Open Sans", Arial, sans-serif;
  }
  .banner__scene {
    position: absolute;
    inset: 0;
    background: linear-gradient(
      to bottom,
      var(--sky-top) 0%,
      var(--sky-mid) 45%,
      var(--sky-low) 75%,
      var(--horizon) 86%,
      var(--sea) 88%,
      var(--sea) 89.5%,
      var(--sand) 93%,
      var(--sand) 100%
    );
  }
  .banner__cap {
    position: absolute;
    top: 0;
    left: 0;
    width: 1200px;
    height: 380px;
  }
  .brand {
    position: absolute;
    left: 82px;
    top: 128px;
    display: flex;
    align-items: center;
    gap: 28px;
  }
  .brand__dot {
    width: 132px;
    height: 132px;
    border-radius: 50%;
    background: var(--ink);
  }
  .brand__name {
    margin: 0;
    font-weight: 600;
    font-size: 70px;
    line-height: 64px;
    color: var(--ink);
  }
  .tagline {
    position: absolute;
    left: 98px;
    top: 440px;
    margin: 0;
    font-style: italic;
    font-weight: 400;
    font-size: 70px;
    color: var(--tagline);
    white-space: nowrap;
  }
  .headline {
    position: absolute;
    left: 98px;
    top: 580px;
    margin: 0;
    font-weight: 700;
    font-size: 142px;
    line-height: 178px;
    color: var(--white);
  }
  .web {
    position: absolute;
    left: 110px;
    top: 1630px;
    margin: 0;
    font-size: 44px;
    letter-spacing: 8px;
    color: var(--url);
    white-space: nowrap;
  }
</style>
</head>
<body>
  <main class="banner">
    <div class="banner__scene" role="img" aria-label="Photo of a clear blue sky over the sea, with a woman on a sandy beach working on a laptop while a young girl plays with a bucket beside her"></div>

    <svg class="banner__cap" viewBox="0 0 1200 380" aria-hidden="true">
      <path d="M0 0 H1200 V0 C1100 260 620 420 0 262 Z" fill="#ffffff"/>
    </svg>

    <header class="brand">
      <span class="brand__dot" aria-hidden="true"></span>
      <p class="brand__name">Plexa<br>Works</p>
    </header>

    <p class="tagline">Easy Efficient Everywhere.</p>

    <h1 class="headline">Create<br>your own<br>online<br>ERP system<br>here for<br>NO CHARGE</h1>

    <p class="web">www.plexaworks-demo.com</p>
  </main>
</body>
</html>
```